I need a label design/logo for a nile glow butter that I making. The body butter is made using Unrefined Shea Butter from Uganda. I have different mixes for the body butter depending on the Essential Oil used, for example - sweet orange, lavender, rosemary. The species of Shea tree in Uganda (Vitellaria Nilotica) is different from the one in West Africa (Vitellaria Paradoxa). As such, I would like the logo/label to have some reference to the Shea nut tree as well as the River Nile. Colours should be "fresh and earthy". I will be using round containers and I would like to be able to place the logo/label on round templates that I can stick on the containers. The name of the brand is "Teka Rumi" nile glow butter.

```html
<!DOCTYPE html>
<html lang="en">
<head>
<meta charset="UTF-8">
<title>Teka Rumi – Nile Glow Butter Label</title>
<link rel="stylesheet" href="https://fonts.googleapis.com/css2?family=Work+Sans:wght@300;400;600&display=swap">
<style>
  :root {
    --page-bg: #ffffff;
    --label-green: #8cc350;
    --ink-grey: #4a4a4a;
    --brand-purple: #7b3c98;
  }
  html, body {
    margin: 0;
    padding: 0;
    width: 1200px;
    height: 1000px;
    overflow: hidden;
    background: var(--page-bg);
  }
  .label-canvas {
    display: block;
    width: 1200px;
    height: 1000px;
  }
  .label-disc { fill: var(--label-green); }
  .divider { stroke: var(--ink-grey); stroke-width: 2.5; }
  .origin-arc-text {
    font-family: "Work Sans", sans-serif;
    font-weight: 400;
    font-size: 28px;
    fill: var(--ink-grey);
  }
  .arc-dot { fill: var(--ink-grey); }
  .product-name {
    font-family: "Work Sans", sans-serif;
    font-weight: 300;
    font-size: 80px;
    fill: var(--ink-grey);
  }
  .trademark { font-size: 36px; }
  .ingredients-heading {
    font-family: "Work Sans", sans-serif;
    font-weight: 600;
    font-size: 19px;
    letter-spacing: 1.5px;
    fill: var(--ink-grey);
  }
  .ingredients-list {
    font-family: "Work Sans", sans-serif;
    font-weight: 600;
    font-size: 16.5px;
    fill: var(--ink-grey);
  }
  .net-weight {
    font-family: "Work Sans", sans-serif;
    font-weight: 400;
    font-size: 26px;
    fill: var(--ink-grey);
  }
  .brand-mark { fill: var(--brand-purple); }
  .brand-name {
    font-family: "Work Sans", sans-serif;
    font-weight: 400;
    font-size: 40px;
    fill: var(--brand-purple);
  }
</style>
</head>
<body>
<svg class="label-canvas" viewBox="0 0 1200 1000" xmlns="http://www.w3.org/2000/svg">
  <defs>
    <path id="origin-arc" d="M 277 534 A 325 325 0 0 1 907 394"/>
  </defs>

  <g class="round-label">
    <circle class="label-disc" cx="600" cy="500" r="380"/>

    <text class="origin-arc-text">
      <textPath href="#origin-arc" textLength="935" lengthAdjust="spacing">MADE FROM UNREFINED SHEA BUTTER FROM UGANDA</textPath>
    </text>
    <circle class="arc-dot" cx="279" cy="586" r="7"/>
    <circle class="arc-dot" cx="926" cy="422" r="7"/>

    <line class="divider" x1="582" y1="345" x2="582" y2="879"/>

    <g class="brand-lockup">
      <circle class="brand-mark" cx="447" cy="460" r="40"/>
      <text class="brand-name" x="447" y="585" text-anchor="middle">Teka Rumi</text>
    </g>

    <text class="net-weight" x="505" y="705" text-anchor="end">50 g</text>

    <text class="product-name" x="602" y="433">nile</text>
    <text class="product-name" x="602" y="517">glow</text>
    <text class="product-name" x="602" y="601">butter<tspan class="trademark" dx="4" dy="-30">™</tspan></text>

    <text class="ingredients-heading" x="604" y="657">INGREDIENTS:</text>
    <text class="ingredients-list" x="604" y="683">SHEA BUTTER, COCONUT OIL</text>
    <text class="ingredients-list" x="604" y="706">&amp; ESSENTIAL OIL</text>
  </g>
</svg>
</body>
</html>
```